I need a business card for ALVA Holdings. We are a young startup based in New Zealand working in internet marketing and web development. The design should have some element connected to New Zealand, such as wave, koru or silver fern, just don't use a kiwi bird.

```html
<!DOCTYPE html>
<html lang="en">
<head>
<meta charset="utf-8">
<title>ALVA Holdings – Business Card</title>
<link rel="stylesheet" href="https://fonts.googleapis.com/css2?family=Open+Sans:ital,wght@0,400;0,600;0,700;1,400&display=swap">
<style>
  :root {
    --bg: #262b33;
    --card: #10151c;
    --blue: #1e7ed0;
    --orange: #e8632b;
    --white: #e9edf2;
    --shadow: rgba(0,0,0,0.45);
  }
  * { margin: 0; padding: 0; box-sizing: border-box; }
  html, body {
    width: 1200px; height: 900px; overflow: hidden;
    background: var(--bg);
    font-family: "Open Sans", sans-serif;
  }
  .card {
    position: absolute;
    width: 560px; height: 320px;
    background: var(--card);
    border-radius: 22px;
    overflow: hidden;
    box-shadow: 0 18px 40px var(--shadow);
  }
  .card--back { left: 580px; top: 90px; }
  .card--front { left: 60px; top: 490px; }

  .accent-panel {
    position: absolute; left: 0; top: 0;
    width: 290px; height: 320px;
    background: linear-gradient(125deg, var(--blue) 0%, #1a6fb8 38%, var(--card) 92%);
  }
  .brand {
    font-weight: 700;
    color: var(--blue);
    white-space: nowrap;
    display: flex; align-items: center; gap: 12px;
  }
  .brand__dot {
    width: 16px; height: 16px; border-radius: 50%;
    background: var(--orange);
  }
  .card--back .brand {
    position: absolute; left: 310px; top: 120px;
    font-size: 28px;
  }
  .card--back .website {
    position: absolute; left: 310px; top: 176px;
    color: var(--white); font-size: 14px; letter-spacing: 3px;
  }

  .card--front .brand {
    position: absolute; left: 40px; top: 134px;
    font-size: 28px;
  }
  .divider {
    position: absolute; left: 290px; top: 70px;
    width: 2px; height: 180px; background: var(--orange);
  }
  .contact {
    position: absolute; left: 318px; top: 78px;
  }
  .contact__name { color: var(--blue); font-size: 28px; font-weight: 400; line-height: 1.1; }
  .contact__title { color: var(--orange); font-size: 16px; margin-bottom: 20px; }
  .contact__row {
    display: flex; align-items: center; gap: 10px;
    color: var(--blue); font-size: 16px; font-style: italic;
    margin-bottom: 8px;
  }
  .contact__row svg { width: 18px; height: 18px; flex: none; }
</style>
</head>
<body>

<section class="card card--back" aria-label="Card back">
  <div class="accent-panel" role="img" aria-label="Blue brand decoration area"></div>
  <div class="brand"><span>ALVA Holdings</span><span class="brand__dot"></span></div>
  <p class="website">www.yourwebsite.com</p>
</section>

<section class="card card--front" aria-label="Card front">
  <div class="brand"><span>ALVA Holdings</span><span class="brand__dot"></span></div>
  <div class="divider"></div>
  <div class="contact">
    <p class="contact__name">Your Name</p>
    <p class="contact__title">Job Title</p>
    <p class="contact__row">
      <svg viewBox="0 0 24 24"><path fill="var(--orange)" d="M3 9c0-3 4-5 9-5s9 2 9 5v2h-5V9H8v2H3zM5 13h14l1 7H4z"/></svg>
      000 000 0000
    </p>
    <p class="contact__row">
      <svg viewBox="0 0 24 24"><rect x="2" y="5" width="20" height="14" fill="var(--orange)"/><path d="M2 5l10 8 10-8" fill="none" stroke="var(--card)" stroke-width="1.6"/></svg>
      youremail@xyz.om
    </p>
    <p class="contact__row">
      <svg viewBox="0 0 24 24" fill="none" stroke="var(--orange)" stroke-width="1.6"><circle cx="12" cy="12" r="9"/><ellipse cx="12" cy="12" rx="4" ry="9"/><path d="M3 12h18M5 7h14M5 17h14"/></svg>
      www.yourwebsite.com
    </p>
  </div>
</section>

</body>
</html>
```